Criação de Papelaria Profissional para Imóveis
" BUSCAMOS CLIENTES PARA COMERCIALIZAÇÃO E LOCAÇÃO DE BENS IMÓVEIS, BEM COMO PRESTAMOS SERVIÇOS DE ADMINISTRAÇÃO DE LOCAÇÕES. CONTUDO EMPREGAMOS E BUSCAMOS A EXCELÊNCIA E A SOFISTICAÇÃO EM NOSSA PRESTAÇÃO DE SERVIÇOS. TEMOS QUE SER DIFERENCIADOS, MUITO ACIMA DE MÉDIA E MUITO SOFISTICADOS. "

```html
<!DOCTYPE html>
<html lang="pt-BR">
<head>
<meta charset="UTF-8">
<title>Castellani &amp; Rocha — Cartão de Visita</title>
<link rel="stylesheet" href="https://fonts.googleapis.com/css2?family=Montserrat:wght@300;400;600&display=swap">
<style>
  :root {
    --lime: #a6cb1f;
    --lime-dark: #8db311;
    --charcoal: #4b4c4e;
    --charcoal-deep: #3c3d3f;
    --paper: #ffffff;
    --paper-shade: #f1f2f2;
    --ink: #5a5b5d;
    --ink-soft: #8a8b8d;
    --backdrop: #2e2f31;
  }
  * { box-sizing: border-box; margin: 0; padding: 0; }
  html, body {
    width: 1200px; height: 1200px; overflow: hidden;
    background: var(--backdrop);
    font-family: "Montserrat", sans-serif;
  }
  .sheet {
    width: 1200px; height: 1200px;
    display: flex; flex-direction: column; align-items: center; justify-content: center;
    gap: 70px;
  }
  .card {
    position: relative;
    width: 900px; height: 514px;
    border-radius: 14px;
    overflow: hidden;
    box-shadow: 0 18px 40px rgba(0,0,0,.35);
  }
  .card__band {
    position: absolute; top: 0; bottom: 0; left: 0;
    width: 46px; background: var(--lime);
  }
  .card__rule {
    position: absolute; top: 0; bottom: 0; left: 62px;
    width: 5px; background: var(--lime);
  }

  /* Front */
  .card--front {
    background: linear-gradient(135deg, var(--charcoal) 0%, var(--charcoal-deep) 100%);
  }
  .brand {
    position: absolute; left: 180px; top: 190px;
    display: flex; align-items: center; gap: 28px;
  }
  .brand__square {
    width: 92px; height: 92px;
    border: 9px solid var(--lime);
    border-radius: 6px;
  }
  .brand__name {
    color: var(--lime);
    font-weight: 400;
    font-size: 44px;
    letter-spacing: 3px;
    text-transform: uppercase;
    line-height: 1;
  }
  .brand__tagline {
    color: var(--lime);
    font-weight: 300;
    font-size: 19px;
    letter-spacing: 3px;
    text-transform: uppercase;
    margin-top: 14px;
  }

  /* Back */
  .card--back {
    background: linear-gradient(120deg, var(--paper) 55%, var(--paper-shade) 100%);
  }
  .contact {
    position: absolute; left: 120px; top: 70px;
    color: var(--ink);
  }
  .contact__name {
    font-weight: 600; font-size: 26px; color: var(--ink);
  }
  .contact__role {
    font-size: 15px; color: var(--ink-soft); margin-top: 4px; margin-bottom: 30px;
  }
  .contact__list { list-style: none; }
  .contact__item {
    display: flex; align-items: flex-start; gap: 14px;
    font-size: 15px; line-height: 1.45; margin-bottom: 14px;
  }
  .contact__icon {
    flex: 0 0 26px; width: 26px; height: 26px;
  }
  .back-brand {
    position: absolute; right: 70px; bottom: 80px;
    text-align: right;
    display: flex; flex-direction: column; align-items: flex-end;
  }
  .back-brand .brand__square { width: 64px; height: 64px; border-width: 7px; margin-bottom: 18px; }
  .back-brand .brand__name { font-size: 30px; letter-spacing: 2px; }
  .back-brand .brand__tagline { font-size: 13px; margin-top: 8px; }
</style>
</head>
<body>
<main class="sheet">

  <section class="card card--front" aria-label="Frente do cartão">
    <div class="card__band"></div>
    <div class="card__rule"></div>
    <div class="brand">
      <div class="brand__square"></div>
      <div>
        <div class="brand__name">Castellani &amp; Rocha</div>
        <div class="brand__tagline">Serviços Imobiliários</div>
      </div>
    </div>
  </section>

  <section class="card card--back" aria-label="Verso do cartão">
    <div class="card__band"></div>
    <div class="card__rule"></div>

    <div class="contact">
      <div class="contact__name">Renato Faria Lemos</div>
      <div class="contact__role">Cargo</div>
      <ul class="contact__list">
        <li class="contact__item">
          <svg class="contact__icon" viewBox="0 0 26 26"><circle cx="13" cy="13" r="12" fill="var(--lime)"/><path d="M9 7.5l2.4 0 1 3-1.5 1.2a7 7 0 0 0 3.4 3.4l1.2-1.5 3 1 0 2.4a1.5 1.5 0 0 1-1.6 1.5A10 10 0 0 1 7.5 9.1 1.5 1.5 0 0 1 9 7.5z" fill="#fff"/></svg>
          <span>(11) 5555-0184 | Fixo<br>(11) 5555-0172 | Celular</span>
        </li>
        <li class="contact__item">
          <svg class="contact__icon" viewBox="0 0 26 26"><circle cx="13" cy="13" r="12" fill="var(--lime)"/><path d="M13 6a5 5 0 0 0-5 5c0 3.8 5 9 5 9s5-5.2 5-9a5 5 0 0 0-5-5zm0 7a2 2 0 1 1 0-4 2 2 0 0 1 0 4z" fill="#fff"/></svg>
          <span>Rua das Acácias, 240 - Centro<br>São Paulo - SP</span>
        </li>
        <li class="contact__item">
          <svg class="contact__icon" viewBox="0 0 26 26"><circle cx="13" cy="13" r="12" fill="var(--lime)"/><rect x="7" y="9" width="12" height="8.5" rx="1" fill="#fff"/><path d="M7.5 9.6l5.5 4.2 5.5-4.2" stroke="var(--lime)" stroke-width="1.2" fill="none"/></svg>
          <span>renato@castellanirocha.com.br</span>
        </li>
        <li class="contact__item">
          <svg class="contact__icon" viewBox="0 0 26 26"><circle cx="13" cy="13" r="12" fill="var(--lime)"/><circle cx="13" cy="13" r="6" stroke="#fff" stroke-width="1.4" fill="none"/><ellipse cx="13" cy="13" rx="2.6" ry="6" stroke="#fff" stroke-width="1.2" fill="none"/><path d="M7 13h12" stroke="#fff" stroke-width="1.2"/></svg>
          <span>www.castellanirocha.com.br</span>
        </li>
      </ul>
    </div>

    <div class="back-brand">
      <div class="brand__square"></div>
      <div class="brand__name">Castellani &amp; Rocha</div>
      <div class="brand__tagline">Serviços Imobiliários</div>
    </div>
  </section>

</main>
</body>
</html>
```